Pre school dance flyer & Whole Dance Academy Flyer

to design a double sided flyer

one side for pre school pupils aged 18 months to five years

the other side a general whole Academy flyer

We are a dance and Performing Arts Academy
Updates

Reason: I've been very busy at work to focus on this

Target Market(s)

Pre school one side
school age to adult other side
Target is Pre school children side one - school age to adult the other

Industry/Entity Type

School

Font styles to use
Sans Serif

Requirements
Must have
• bright colourful and exciting
Should not have
• dark colours

```html
<!DOCTYPE html>
<html lang="en">
<head>
<meta charset="utf-8">
<title>Brightstep Academy – Double Sided Flyer</title>
<link rel="stylesheet" href="https://fonts.googleapis.com/css2?family=Alfa+Slab+One&family=Cabin:wght@400;600&family=Courgette&display=swap">
<style>
  :root {
    --bg: #9a9a9c;
    --purple: #7b3f98;
    --purple-deep: #5a2a78;
    --pink: #e8589b;
    --pink-hot: #e2458d;
    --ink: #1c1320;
    --heading-ink: #3a1745;
    --white: #ffffff;
    --shadow: rgba(0,0,0,.45);
  }
  * { box-sizing: border-box; margin: 0; padding: 0; }
  html, body { width: 1200px; height: 800px; overflow: hidden; }
  body { background: var(--bg); font-family: "Cabin", sans-serif; position: relative; }

  .flyer { position: absolute; top: 25px; height: 752px; background: var(--white); overflow: hidden; box-shadow: 6px 6px 10px var(--shadow); }
  .flyer--front { left: 57px; width: 528px; }
  .flyer--back { left: 627px; width: 530px; }
  .flyer > * { position: absolute; }

  .photo { left: 0; }
  .hero-photo { top: 0; width: 100%; }
  .front-hero { height: 300px; background: linear-gradient(135deg, #c9a08f 0%, #e9b7cf 35%, #d98cc0 60%, #6a3a5e 100%); }
  .back-hero { height: 260px; background: radial-gradient(ellipse at 60% 40%, #d3608f 0%, #8a2a5a 45%, #2a0f22 100%); }

  .wave { left: 0; width: 100%; }

  .strip { display: flex; width: 100%; height: 105px; }
  .strip .photo { position: static; flex: 1; height: 100%; }
  .front-strip { top: 452px; }
  .back-strip { top: 485px; }
  .tone-a { background: linear-gradient(160deg, #2b2a4a, #b9a3c9 60%, #3f3550); }
  .tone-b { background: linear-gradient(160deg, #3a3f72, #d8c2d9 50%, #7aa6d8); }
  .tone-c { background: linear-gradient(160deg, #6a1e26, #d94a52 50%, #f1c6c8); }
  .tone-d { background: linear-gradient(160deg, #c44b8a, #e8a1c0 50%, #7a1830); }
  .tone-e { background: linear-gradient(160deg, #1a1416, #8c4a3e 50%, #d7b49a); }
  .tone-f { background: linear-gradient(160deg, #2f5fa8, #a9c6e8 50%, #6a8a3a); }

  .join-badge { left: 203px; top: 195px; width: 140px; height: 140px; border-radius: 50%; background: var(--pink-hot); border: 6px solid var(--white); color: var(--white); text-align: center; font-family: "Alfa Slab One", serif; display: flex; flex-direction: column; justify-content: center; line-height: 1; }
  .join-badge .big { font-size: 33px; }
  .join-badge .small { font-family: "Cabin", sans-serif; font-weight: 600; font-size: 12px; margin: 3px 0; }

  .brand { color: var(--ink); }
  .brand-name { font-family: "Cabin", sans-serif; font-weight: 400; line-height: 1; }
  .brand-tag { font-size: 7px; letter-spacing: .3px; text-transform: uppercase; margin-top: 4px; }
  .front-brand { left: 18px; top: 345px; }
  .front-brand .brand-name { font-size: 50px; }

  .offer { left: 290px; top: 378px; text-align: left; }
  .offer-title { font-family: "Courgette", cursive; color: var(--purple); font-size: 25px; line-height: 1; }
  .offer-sub { font-family: "Alfa Slab One", serif; font-size: 16px; color: var(--ink); margin-top: 3px; }

  .pink-panel { left: 0; width: 100%; background: var(--pink); }
  .front-panel { top: 557px; height: 158px; }
  .tag-line { background: var(--purple); color: var(--white); font-size: 17px; height: 24px; line-height: 24px; padding: 0 14px; }
  .tag-line--one { left: 0; top: 565px; width: 315px; padding-left: 30px; }
  .tag-line--two { left: 115px; top: 595px; width: 413px; text-align: right; }

  .contact-block { text-align: center; color: var(--white); }
  .contact-heading { font-family: "Alfa Slab One", serif; color: var(--heading-ink); font-size: 24px; line-height: 1.1; margin-bottom: 6px; }
  .venue { left: 20px; width: 235px; top: 627px; font-size: 14px; line-height: 1.5; }
  .venue .line-2 { font-size: 16px; }
  .call { left: 300px; width: 215px; top: 627px; font-size: 21px; }

  .footer-bar { left: 0; top: 715px; width: 100%; height: 37px; background: var(--purple); color: var(--white); text-align: center; font-size: 16px; line-height: 37px; }

  .back-join { left: 60px; top: 280px; font-family: "Courgette", cursive; font-weight: 400; color: var(--purple); font-size: 26px; line-height: 1.1; }
  .back-copy { left: 30px; top: 320px; width: 180px; font-size: 11.5px; line-height: 1.3; text-align: justify; color: var(--ink); }
  .back-motto { left: 26px; top: 402px; font-family: "Courgette", cursive; color: var(--purple); font-size: 20px; line-height: 1.2; }
  .partner-badge { left: 318px; top: 372px; width: 187px; height: 66px; }

  .welcome-bar { left: 0; top: 457px; width: 100%; height: 28px; background: var(--pink); color: var(--white); font-family: "Alfa Slab One", serif; font-size: 18px; text-align: center; line-height: 28px; }

  .purple-panel { left: 0; top: 590px; width: 100%; height: 162px; background: var(--purple); }
  .back-call { left: 28px; top: 600px; color: var(--white); font-size: 15px; }
  .back-call .contact-heading { color: var(--pink); font-size: 20px; margin: 0; text-align: center; }
  .social { display: flex; align-items: center; gap: 6px; color: var(--white); font-family: "Alfa Slab One", serif; }
  .social-square { width: 24px; height: 24px; background: var(--white); border-radius: 3px; flex: none; }
  .social-handle { font-size: 17px; line-height: 1; }
  .social-handle small { display: block; font-size: 10px; }
  .social--one { left: 160px; top: 604px; }
  .social--two { left: 328px; top: 608px; }

  .back-brand { left: 80px; top: 668px; color: var(--white); text-align: center; }
  .back-brand .brand-name { font-size: 40px; }
  .back-brand .brand-tag { font-size: 6px; }
  .accreditation { left: 285px; top: 675px; width: 150px; height: 42px; background: var(--white); }
</style>
</head>
<body>

<section class="flyer flyer--front" aria-label="Front of flyer">
  <div class="photo hero-photo front-hero" role="img" aria-label="Photo of young pre-school dancers in pink and lilac tutus on stage"></div>

  <svg class="wave" style="top:230px" width="528" height="140" viewBox="0 0 528 140" aria-hidden="true">
    <path d="M0 44 C160 14 330 62 528 4 L528 98 C380 122 200 72 0 98 Z" fill="#7b3f98"/>
    <path d="M0 36 C160 6 330 54 528 -4" stroke="#ffffff" stroke-width="4" fill="none"/>
    <path d="M0 98 C200 72 380 122 528 98 L528 140 L0 140 Z" fill="#ffffff"/>
  </svg>

  <div class="join-badge">
    <span class="big">Join</span>
    <span class="small">the academy</span>
    <span class="big">today</span>
  </div>

  <div class="brand front-brand">
    <div class="brand-name">Brightstep</div>
    <div class="brand-tag">Academy of Dance and Performing Arts</div>
  </div>

  <div class="offer">
    <div class="offer-title">Free Trial Class</div>
    <div class="offer-sub">for all new pupils</div>
  </div>

  <div class="strip front-strip">
    <div class="photo tone-a" role="img" aria-label="Photo of pupils in white dance dresses performing"></div>
    <div class="photo tone-b" role="img" aria-label="Photo of a line of young dancers in coloured tutus"></div>
    <div class="photo tone-c" role="img" aria-label="Photo of dancers in red costumes on stage"></div>
  </div>

  <div class="pink-panel front-panel"></div>
  <p class="tag-line tag-line--one">Pursue a career in the performing</p>
  <p class="tag-line tag-line--two">arts or simply attend for enjoyment and fun.</p>

  <div class="contact-block venue">
    <h2 class="contact-heading">Venue</h2>
    <p>The Parish Hall of St Aldric</p>
    <p class="line-2">Elmbrook EB4 2QT</p>
  </div>

  <div class="contact-block call">
    <h2 class="contact-heading">Call</h2>
    <p>01632 960 418</p>
  </div>

  <p class="footer-bar">www.brightstepdanceacademy.co.uk</p>
</section>

<section class="flyer flyer--back" aria-label="Back of flyer">
  <div class="photo hero-photo back-hero" role="img" aria-label="Photo of older dance students performing on a pink-lit stage"></div>

  <svg class="wave" style="top:170px" width="530" height="200" viewBox="0 0 530 200" aria-hidden="true">
    <path d="M0 85 C180 120 360 60 530 5 L530 185 C420 120 200 100 0 100 Z" fill="#7b3f98"/>
    <path d="M0 78 C180 113 360 53 530 -2" stroke="#ffffff" stroke-width="4" fill="none"/>
    <path d="M0 100 C200 100 420 120 530 185 L530 200 L0 200 Z" fill="#ffffff"/>
  </svg>

  <h2 class="back-join">Join Us</h2>
  <p class="back-copy">Qualified dance teachers all DBS checked and first aid trained, deliver an exciting curriculum which is fun, stimulating and challenging.</p>
  <p class="back-motto">Learn develop and have fun!</p>

  <svg class="partner-badge" viewBox="0 0 187 66" role="img" aria-label="Dance school accreditation badge">
    <rect x="0" y="0" width="187" height="66" fill="#1c1320"/>
  </svg>

  <p class="welcome-bar">We welcome you to Brightstep</p>

  <div class="strip back-strip">
    <div class="photo tone-d" role="img" aria-label="Photo of dancers with parasols in red costumes"></div>
    <div class="photo tone-e" role="img" aria-label="Photo of young dancers in cowboy hats"></div>
    <div class="photo tone-f" role="img" aria-label="Photo of a ballet scene with a dancer in a white tutu"></div>
  </div>

  <div class="purple-panel"></div>

  <div class="back-call">
    <h2 class="contact-heading">Call</h2>
    <p>01632 960 418</p>
  </div>

  <div class="social social--one">
    <span class="social-square"></span>
    <span class="social-handle">@brightstep<small>academyofdance</small></span>
  </div>
  <div class="social social--two">
    <span class="social-square"></span>
    <span class="social-handle">hbrookearts</span>
  </div>

  <div class="brand back-brand">
    <div class="brand-name">Brightstep</div>
    <div class="brand-tag">Academy of Dance and Performing Arts</div>
  </div>

  <div class="accreditation" role="img" aria-label="Performing arts exam board badge"></div>
</section>

</body>
</html>
```